$$$ F&B Needs New Theme for its takeaway bowls, Cups and Theme!

Hi everyone,
K here, representing 北岭米糕 beilingmigao, a soy based f&b company situated in China, selling delicious tofu pudding, soy beverages and simple bites.
北岭米糕 is currently looking to revamp its current set of bowls and cups and materials and we would love to receive your input on this!
We are looking for a theme and concept to print onto our:
1) disposable large sized plastic bowl model: Q725
Printable Area: 2.5cm tall by 32cm of circumference
2) disposable 16oz plastic cup model: R318D
Printable Area 1 : 8cm tall by 22cm of circumference
Printable Area 2: 9cm tall by 20cm of circumference
3) paper bag/box to wrap our pies in size:
Printable Area: height 11cm by breadth 9cm by thickness 4.5cm
Please restrict to using 4 colours max.
The below links point to some themes we especially like:
1)
http://www.plumora-sample.com.tw/portfolio-one/
2)
http://www.plumora-sample.com.tw/portfolio-two/
3)
http://www.plumora-sample.com.tw/portfolio-three/
as you can see, we would like an oriental/ asian/ chinese feel, with things like wood, white, red stamps, brown paper, calligraphy and things like that.
it would help if you could mock up your design on to a disposable bowl to show us.
here is the info you should also display
1) our logo.
2) the text "beilingmigao"
3) www.beilingmigao-demo.com
4) 微信号: blmg6161
5) 微博:北岭米糕
6) 加盟热线:139 8765 2041
we are an existing business with some photos at this link to help you better visualize what we want.
i also uploaded some nanyang chinatown street photos and and sketched street photo... going along the line of antique china/chinese streets feel..
http://www.beilingmigao-demo.com/
Updates
Hi all!
we have up-ed our budget and provided more information on the printable area so it is easier for you to work with.
we are looking to improve our positioning and packaging so pls submit a new design and not a small modification of our current bowl.
please look at the links we have provided, they serve to give you a good idea of what we like.
j
Reason: as requested. waiting for better designs!
Reason: I looking for sketches of chinese streets as background, with 2-3 colours for the sketches.
Not looking into using photos for the packaging.
Reason: for edits
Plastic

```html
<!DOCTYPE html>
<html lang="zh">
<head>
<meta charset="utf-8">
<title>北岭米糕 Packaging Panel</title>
<link rel="stylesheet" href="https://fonts.googleapis.com/css2?family=Noto+Sans+SC:wght@500;700&family=Quicksand:wght@600&family=Noto+Serif:wght@400&display=swap">
<style>
  :root {
    --stage: #5e6061;
    --panel: #2f3739;
    --gold: #bb9c68;
    --gold-light: #d8c29a;
    --gold-deep: #8c7248;
    --seal: #b52a2e;
    --ink-light: #e9e6df;
  }
  html, body {
    margin: 0;
    width: 1200px;
    height: 900px;
    overflow: hidden;
    background: var(--stage);
  }
  .canvas {
    position: relative;
    width: 1200px;
    height: 900px;
  }
  .panel {
    position: absolute;
    left: 280px;
    top: 130px;
    width: 640px;
    height: 640px;
    background: var(--panel);
  }
  .landscape {
    position: absolute;
    left: 241px;
    top: 8px;
    width: 158px;
    height: 342px;
    background: linear-gradient(180deg, rgba(187,156,104,0.35) 0%, rgba(187,156,104,0.7) 45%, rgba(140,114,72,0.85) 100%);
  }
  .brand {
    position: absolute;
    left: 0;
    right: 0;
    top: 372px;
    display: flex;
    justify-content: center;
    align-items: center;
    gap: 10px;
  }
  .brand-name {
    font-family: "Noto Sans SC", sans-serif;
    font-weight: 700;
    font-size: 60px;
    letter-spacing: 4px;
    color: var(--gold);
    line-height: 1;
  }
  .brand-seal {
    width: 30px;
    height: 30px;
    background: var(--seal);
    margin-top: 14px;
  }
  .brand-latin {
    position: absolute;
    left: 0;
    right: 0;
    top: 462px;
    text-align: center;
    font-family: "Quicksand", sans-serif;
    font-weight: 600;
    font-size: 18px;
    letter-spacing: 0.5px;
    color: var(--ink-light);
  }
  .contact {
    position: absolute;
    left: 340px;
    top: 520px;
    margin: 0;
    padding: 0;
    list-style: none;
    font-family: "Noto Serif", serif;
    font-size: 10px;
    line-height: 14px;
    color: var(--ink-light);
  }
  .contact li {
    display: flex;
    align-items: center;
    gap: 6px;
  }
  .contact .web {
    font-size: 12px;
    font-weight: 400;
  }
  .contact svg {
    width: 9px;
    height: 9px;
    fill: var(--ink-light);
  }
</style>
</head>
<body>
<main class="canvas">
  <section class="panel">
    <div class="landscape" role="img" aria-label="Gold line illustration of a moonlit Chinese landscape with trees, a pavilion, rocks and a small boat on water"></div>

    <div class="brand">
      <span class="brand-name">北岭米糕</span>
      <span class="brand-seal" aria-hidden="true"></span>
    </div>
    <div class="brand-latin">beilingmigao</div>

    <ul class="contact">
      <li>
        <svg viewBox="0 0 10 10" aria-hidden="true"><path d="M5 1 L9 5 L8 5 L8 9 L2 9 L2 5 L1 5 Z"/></svg>
        <span>Micro Signal: blmg6161</span>
      </li>
      <li>
        <svg viewBox="0 0 10 10" aria-hidden="true"><circle cx="5" cy="5" r="4"/></svg>
        <span>Microblog: Beiling migao</span>
      </li>
      <li>
        <svg viewBox="0 0 10 10" aria-hidden="true"><path d="M2 1 L4 1 L5 3 L4 4 Q5 6 6 6 L7 5 L9 6 L9 8 Q8 9 7 9 Q1 7 1 2 Q1 1 2 1 Z"/></svg>
        <span>Join Hotline: 139 8765 2041</span>
      </li>
      <li class="web">
        <svg viewBox="0 0 10 10" aria-hidden="true"><circle cx="5" cy="5" r="4" fill="none" stroke="#e9e6df" stroke-width="1.2"/><path d="M1 5 H9 M5 1 V9" stroke="#e9e6df" stroke-width="0.8"/></svg>
        <span>www.beilingmigao-demo.com</span>
      </li>
    </ul>
  </section>
</main>
</body>
</html>
```